8 1/2 x 8 1/2 Social Media Design Ad - Commercial Loan Originator

Wanted
Commercial Loan Originators

* No Licensing Required
* Lend Nationwide with few exceptions
* Competitive Compensation
* You find the Investors and we handle the rest!!!

PRODUCTS
* Debt Service Coverage Loans (DSCR)
* Fix & Flip Financing
* Ground Up Construction
* Bridge Loans
* Portfolio Loans
And many more.....

Call (800) 417-9265 x24 for more information

Brightmoor Lending Partners, Inc.
7200 Warbleton Avenue, Linwood Falls, MD 21758
NMLS #318640

```html
<!DOCTYPE html>
<html lang="en">
<head>
<meta charset="utf-8">
<title>Commercial Loan Originators Wanted</title>
<link rel="stylesheet" href="https://fonts.googleapis.com/css2?family=Playfair+Display:wght@700;900&family=Lexend:wght@300;400;600;700&family=Oswald:wght@600&display=swap">
<style>
:root{
  --page:#f4f4f4;
  --navy:#01141f;
  --blue:#0a2fa8;
  --blue-bright:#2e6fd8;
  --blue-deep:#0a1f6e;
  --gold:#c99232;
  --gold-light:#f3c761;
  --gold-dark:#9c600f;
  --white:#ffffff;
  --ink:#0b1420;
}
*{margin:0;padding:0;box-sizing:border-box}
html,body{width:1200px;height:1200px;overflow:hidden;background:var(--page)}
.ad{position:absolute;left:57px;top:57px;width:1089px;height:1089px;background:var(--navy);overflow:hidden;font-family:"Lexend",sans-serif}
.ad > *{position:absolute}
.top-band{left:0;top:0;width:1089px;height:171px;background:linear-gradient(90deg,#1d4fc4 0%,var(--blue-bright) 45%,#0b2fa6 100%)}
.gold-band{left:0;top:178px;width:1089px;height:73px;background:linear-gradient(90deg,var(--gold-dark) 0%,var(--gold-light) 45%,var(--gold) 75%,var(--gold-dark) 100%)}
.logo-disc{left:39px;top:39px;width:398px;height:398px;border-radius:50%;background:var(--navy)}
.brand{left:70px;top:150px;width:336px;text-align:center;font-family:"Playfair Display",serif;font-weight:900;font-size:32px;line-height:1.15;color:var(--gold-light)}
.est{left:70px;top:264px;width:336px;text-align:center;font-family:"Lexend",sans-serif;font-weight:600;font-size:13px;letter-spacing:4px;color:var(--gold-light)}
.headline{left:421px;top:16px;width:618px;text-align:center;font-family:"Playfair Display",serif;font-weight:900;font-size:128px;line-height:1;color:var(--white);letter-spacing:1px}
.subhead{left:450px;top:188px;width:590px;text-align:center;font-weight:700;font-size:37px;line-height:52px;color:var(--ink)}
.features{left:0;top:303px;width:1089px;height:237px;background:linear-gradient(90deg,#061a45 0%,#0a2a9c 45%,var(--blue) 100%)}
.feature{display:flex;align-items:center;gap:18px;width:300px}
.feature .badge{flex:none;width:86px;height:86px;border-radius:50%;background:var(--gold);border:4px solid var(--navy);box-shadow:0 0 0 3px var(--blue-bright)}
.feature p{font-weight:300;font-size:20px;line-height:25px;color:var(--white)}
.f1{left:61px;top:324px}
.f2{left:347px;top:324px;width:340px}
.f3{left:61px;top:433px}
.f4{left:347px;top:433px;width:340px}
.photo{background:linear-gradient(135deg,#c8b79d,#5d6b5a);border:2px solid var(--blue);border-radius:16px}
.photo-hero{left:722px;top:304px;width:329px;height:235px;border-radius:0 16px 16px 0;background:linear-gradient(160deg,#b9c3cc 0%,#7b8798 45%,#6aa13b 100%);border:none}
.photo-a{left:36px;top:569px;width:331px;height:203px;background:linear-gradient(135deg,#eae4dc,#9a6a3a 55%,#2a2a2a)}
.photo-b{left:379px;top:569px;width:331px;height:203px;background:linear-gradient(135deg,#8fb4d4,#e6ebf2 50%,#3b2e2a)}
.photo-c{left:722px;top:569px;width:331px;height:203px;background:linear-gradient(135deg,#e6e6e6,#6d6a66 50%,#2f3a2e)}
.products-title{left:49px;top:792px;font-family:"Playfair Display",serif;font-weight:900;font-size:46px;line-height:54px;color:var(--gold)}
.products-frame{left:34px;top:818px;width:550px;height:226px}
.product-list{left:49px;top:858px;list-style:none}
.product-list li{display:flex;align-items:center;gap:12px;font-weight:400;font-size:27px;line-height:32px;color:var(--white)}
.product-list svg{flex:none}
.more{font-weight:700;color:var(--gold-light)}
.contact{left:594px;top:819px;width:457px;height:223px;border-radius:22px;overflow:hidden;background:var(--gold)}
.contact-head{height:41px;background:#000;display:flex;align-items:center;justify-content:center;gap:14px;font-family:"Playfair Display",serif;font-weight:700;font-size:23px;color:var(--white)}
.contact-head i{display:block;width:72px;height:2px;background:var(--gold)}
.contact-phone{height:92px;background:var(--blue);text-align:center;color:var(--white)}
.contact-phone .number{font-family:"Oswald",sans-serif;font-weight:600;font-size:52px;line-height:66px;letter-spacing:-0.5px}
.contact-phone .more-info{font-family:"Playfair Display",serif;font-weight:700;font-size:19px;letter-spacing:4px;line-height:22px}
.contact-details{padding-top:9px;text-align:center;font-weight:600;font-size:16px;line-height:25px;color:var(--white)}
.footer-arc{left:12px;top:1076px;width:1065px;height:60px;border-radius:30px 30px 0 0;background:linear-gradient(90deg,var(--gold-dark),var(--gold-light) 50%,var(--gold-dark))}
</style>
</head>
<body>
<main class="ad">
  <div class="top-band"></div>
  <div class="gold-band"></div>
  <div class="logo-disc"></div>
  <div class="brand">Brightmoor Lending Partners</div>
  <div class="est">EST. 1997</div>

  <h1 class="headline">WANTED</h1>
  <h2 class="subhead">Commercial Loan Originators</h2>

  <section class="features"></section>
  <div class="feature f1"><span class="badge"></span><p>No Licensing<br>Required</p></div>
  <div class="feature f2"><span class="badge"></span><p>Lend Nationwide<br>with few exceptions</p></div>
  <div class="feature f3"><span class="badge"></span><p>Competitive<br>Compensation</p></div>
  <div class="feature f4"><span class="badge"></span><p>You find the Investors<br>and we handle the rest</p></div>

  <div class="photo photo-hero" role="img" aria-label="Smiling businessman in a suit with arms crossed in front of a house"></div>
  <div class="photo photo-a" role="img" aria-label="Businesswoman in a consultation at an office desk"></div>
  <div class="photo photo-b" role="img" aria-label="Businessman reviewing a tablet by an office window"></div>
  <div class="photo photo-c" role="img" aria-label="Advisor reviewing documents with an older couple"></div>

  <svg class="products-frame" width="550" height="226" viewBox="0 0 550 226" aria-hidden="true">
    <path d="M332 1 H530 Q549 1 549 20 V206 Q549 225 530 225 H0" fill="none" stroke="#c99232" stroke-width="1.5"/>
  </svg>
  <h3 class="products-title">PRODUCTS</h3>
  <ul class="product-list">
    <li><svg width="22" height="22" viewBox="0 0 22 22"><circle cx="11" cy="11" r="9" fill="none" stroke="#2e6fd8" stroke-width="2"/><path d="M6 11l4 4 8-10" fill="none" stroke="#2e6fd8" stroke-width="2.4"/></svg>Debt Service Coverage Loans (DSCR)</li>
    <li><svg width="22" height="22" viewBox="0 0 22 22"><circle cx="11" cy="11" r="9" fill="none" stroke="#2e6fd8" stroke-width="2"/><path d="M6 11l4 4 8-10" fill="none" stroke="#2e6fd8" stroke-width="2.4"/></svg>Fix &amp; Flip Financing</li>
    <li><svg width="22" height="22" viewBox="0 0 22 22"><circle cx="11" cy="11" r="9" fill="none" stroke="#2e6fd8" stroke-width="2"/><path d="M6 11l4 4 8-10" fill="none" stroke="#2e6fd8" stroke-width="2.4"/></svg>Ground Up Construction</li>
    <li><svg width="22" height="22" viewBox="0 0 22 22"><circle cx="11" cy="11" r="9" fill="none" stroke="#2e6fd8" stroke-width="2"/><path d="M6 11l4 4 8-10" fill="none" stroke="#2e6fd8" stroke-width="2.4"/></svg>Bridge Loans</li>
    <li><svg width="22" height="22" viewBox="0 0 22 22"><circle cx="11" cy="11" r="9" fill="none" stroke="#2e6fd8" stroke-width="2"/><path d="M6 11l4 4 8-10" fill="none" stroke="#2e6fd8" stroke-width="2.4"/></svg>Portfolio Loans&nbsp;<span class="more">And many more.....</span></li>
  </ul>

  <section class="contact">
    <div class="contact-head"><i></i>CALL US TODAY AT<i></i></div>
    <div class="contact-phone">
      <div class="number">(800) 417-9265 X24</div>
      <div class="more-info">For More Information</div>
    </div>
    <div class="contact-details">
      Brightmoor Lending Partners, Inc.<br>
      7200 Warbleton Avenue, Linwood Falls, MD 21758<br>
      NMLS #318640
    </div>
  </section>

  <div class="footer-arc"></div>
</main>
</body>
</html>
```